Hollow Lantern Double Sided Flyer Design

We need a double sided flyer (1/3 of an A4 which is 99mm x 210mm) developed for our Newcastle(NSW) tour. This flyer will be placed in tourist information centres and hotels. We want it to direct people to our website or be able to make bookings over the phone.

About Us:-
We are a city walking tour company that runs tours day or night. We run both day and night and will incorporate real history / real Hollow Lantern. Some of the stories will be quite serious i.e.- there are infamous murders from 100 years ago, baffling court cases, even a bit of poetry written by murderers, suicides, love triangles, you name it. We will be telling the historical stories that tourists will not hear from any other tour provider. A bit of darkness, a bit of mystery and a bit of history theme.

We do no go for scares and let the very real stories deliver the entertainment for our guests. Our customers enjoy our tours, but it isn't light fun and frivolity. Our stories are being carefully crafted and are packed with unexpected twists, turns; revelations whilst remaining all 100% true. We deliver deep, rich, engaging stories.

Here are a few samples of quotes from the characters in our stories that may give you an idea of the kind of history we will cover:-

"There were bits of spines, bits of skulls, [and] finger bones spilled out all over the streets - I ended up filling three boxes. Children were playing with them for weeks”

"I had a close shave last night and now I want a close haircut.”

“She's a beautiful child', isn't she? She's the cause of all the trouble.”

“I did it because she would not come home with me.”

"I have killed my wife. I’m glad she’s dead.”

"Stand aside or I'll put a bullet through both of you."

“You villain, I'll teach you to take away my character."

“You’re not dead yet, you bastard!”

Our website, booking form and contact details can be viewed at www.hollowlantern-walks.com.au

Target Market(s)

Tourists

Industry/Entity Type

Tour

Colors

Designer to choose colors to be used in the design.

Requirements
Must have
• Vertical orientation please.
• Please also include a reference to a discount offer of 25% using the promo code "MOTH".
Nice to have
• FRONT FLYER INFORMATION
• - Hollow Lantern Logo
• - "I have killed my wife; I'm glad she's dead."
• - Quayside Vanished Years Walk
• - 25% Discount Offer Codeword MOTH
• - web address at the base; www.hollowlantern-walks.com.au
• BACK FLYER INFORMATION
• - "She's a beautiful child', isn't she? She's the cause of all the trouble.
• - Hollow Lantern Logo at the base along with the web address www.hollowlantern-walks.com.au
• - Blurb:- Hollow Lantern brings back Newcastle's hidden past, the forgotten past, the dark past that may not want to be remembered.
• Real stories from the streets around you. Discover the histories you won't hear anywhere else. The forgotten stories of yesteryear finally get a chance to be told. Through you they get to live again.
Should not have
• GENERAL
• Please do not include the phone number, email address or social media icons. We want to drive online bookings.

```html
<!DOCTYPE html>
<html lang="en">
<head>
<meta charset="utf-8">
<title>Hollow Lantern – Double Sided Flyer</title>
<link rel="stylesheet" href="https://fonts.googleapis.com/css2?family=Montserrat:wght@500;600;700;800&family=PT+Serif:ital@1&display=swap">
<style>
  :root {
    --ink: #1d1a17;
    --band: #221e1b;
    --paper: #efe2c6;
    --paper-deep: #e2cda2;
    --red: #c8222a;
    --red-bar: #b81f26;
    --cream: #f3ead6;
    --gold: #d9b77a;
    --stage: #d9d4cb;
    --sepia-dark: #3b342d;
    --sepia-mid: #8c8273;
    --sepia-light: #cfc6b4;
  }
  * { margin: 0; padding: 0; box-sizing: border-box; }
  html, body { width: 1200px; height: 998px; overflow: hidden; }
  body { background: var(--stage); position: relative; font-family: "Montserrat", sans-serif; color: var(--ink); }

  .flyer {
    position: absolute; top: 49px; width: 416px; height: 883px; overflow: hidden;
    background:
      radial-gradient(ellipse at 80% 30%, rgba(214,180,120,.45), transparent 55%),
      radial-gradient(ellipse at 20% 70%, rgba(220,196,150,.4), transparent 60%),
      var(--paper);
    box-shadow: 0 6px 14px rgba(0,0,0,.35);
  }
  .flyer--front { left: 156px; }
  .flyer--back { left: 628px; }

  .quote-band {
    position: absolute; left: 0; top: 0; width: 100%; height: 150px; background: var(--band);
    clip-path: polygon(0 0,100% 0,100% 84%,96% 88%,92% 83%,87% 89%,82% 85%,77% 90%,71% 84%,66% 88%,60% 83%,55% 89%,49% 85%,44% 90%,38% 84%,33% 88%,27% 83%,22% 89%,16% 84%,11% 88%,6% 83%,2% 87%,0 85%);
  }
  .quote {
    position: absolute; left: 0; width: 100%; top: 28px; text-align: center;
    font-family: "PT Serif", serif; font-style: italic; color: var(--cream);
    font-size: 31px; line-height: 35px;
  }
  .flyer--back .quote { font-size: 27px; line-height: 33px; top: 28px; }

  .brand {
    position: absolute; left: 0; width: 100%; top: 262px;
    display: flex; align-items: center; justify-content: center; gap: 12px;
  }
  .brand__dot { width: 22px; height: 22px; border-radius: 50%; background: var(--ink); }
  .brand__name { font-weight: 500; font-size: 33px; color: var(--ink); letter-spacing: .5px; }

  .stain {
    position: absolute; left: -40px; top: 380px; width: 220px; height: 250px;
    background: radial-gradient(ellipse at center, rgba(226,100,110,.45), rgba(226,100,110,0) 70%);
  }
  .flyer--back .stain { left: -70px; top: 150px; width: 150px; height: 170px; }

  .tour-title {
    position: absolute; left: 0; width: 100%; top: 348px; text-align: center;
    font-weight: 800; font-size: 22.5px; line-height: 28px; text-transform: uppercase;
  }
  .tour-title__accent { color: var(--red); }

  .street-photo {
    position: absolute; left: 0; top: 560px; width: 100%; height: 286px;
    background: linear-gradient(100deg, var(--sepia-dark) 0%, #5a5046 35%, var(--sepia-mid) 70%, var(--sepia-light) 100%);
    -webkit-mask-image: linear-gradient(to bottom, transparent 0%, #000 25%);
            mask-image: linear-gradient(to bottom, transparent 0%, #000 25%);
  }

  .discount-badge { position: absolute; left: 228px; top: 442px; width: 164px; height: 164px; }

  .web-bar {
    position: absolute; left: 0; bottom: 0; width: 100%; height: 38px; background: var(--red-bar);
    color: #fff; font-weight: 700; font-size: 17.5px; letter-spacing: .3px;
    display: flex; align-items: center; justify-content: center;
  }

  .blurb {
    position: absolute; left: 50px; right: 50px; text-align: center;
    font-weight: 700; font-size: 14.8px; line-height: 22.5px; color: var(--ink);
  }
  .blurb--intro { top: 150px; }
  .blurb--body { top: 535px; left: 36px; right: 36px; }

  .tram-photo {
    position: absolute; left: 0; top: 282px; width: 100%; height: 216px;
    background: linear-gradient(95deg, #2a2622 0%, #4d463e 30%, #a69c8a 60%, #7b7265 85%, #3a342e 100%);
    clip-path: polygon(0 6%,6% 3%,12% 7%,19% 2%,26% 6%,33% 3%,40% 7%,47% 2%,54% 6%,61% 3%,68% 8%,75% 2%,82% 6%,89% 3%,95% 7%,100% 4%,100% 94%,94% 97%,88% 93%,81% 98%,74% 94%,67% 97%,60% 92%,53% 98%,46% 94%,39% 97%,32% 93%,25% 98%,18% 94%,11% 97%,5% 93%,0 96%);
  }

  .brand--footer { top: 730px; gap: 10px; }
  .brand--footer .brand__ring { width: 40px; height: 40px; border-radius: 50%; border: 4px solid var(--ink); }
  .brand--footer .brand__name { font-size: 24px; }
</style>
</head>
<body>

<section class="flyer flyer--front" aria-label="Flyer front">
  <div class="quote-band"></div>
  <p class="quote">"I have killed my wife;<br>I'm glad she's dead."</p>

  <div class="brand">
    <span class="brand__dot"></span>
    <span class="brand__name">Hollow Lantern</span>
  </div>

  <div class="stain" role="img" aria-label="Soft red watercolour wash"></div>

  <h1 class="tour-title">
    Walking Quayside<br>
    <span class="tour-title__accent">Vanished Years</span><br>
    Walk
  </h1>

  <div class="street-photo" role="img" aria-label="Sepia photograph of an old sandstone street with Victorian buildings"></div>

  <svg class="discount-badge" viewBox="0 0 164 164" aria-label="25% discount offer, codeword MOTH">
    <defs>
      <path id="code-arc" d="M30 82 A52 52 0 0 0 134 82"/>
    </defs>
    <circle cx="82" cy="82" r="80" fill="var(--band)"/>
    <circle cx="82" cy="82" r="73" fill="none" stroke="var(--cream)" stroke-width="2"/>
    <text x="82" y="68" text-anchor="middle" fill="#fff" font-family="Montserrat, sans-serif" font-weight="700" font-size="34">25%</text>
    <text x="82" y="89" text-anchor="middle" fill="#fff" font-family="Montserrat, sans-serif" font-weight="700" font-size="13.5">DISCOUNT</text>
    <text x="82" y="105" text-anchor="middle" fill="#fff" font-family="Montserrat, sans-serif" font-weight="700" font-size="13.5">OFFER</text>
    <text fill="var(--gold)" font-family="Montserrat, sans-serif" font-weight="600" font-size="12" letter-spacing="1">
      <textPath href="#code-arc" startOffset="50%" text-anchor="middle">CODEWORD: MOTH</textPath>
    </text>
  </svg>

  <div class="web-bar">WWW.HOLLOWLANTERN-WALKS.COM.AU</div>
</section>

<section class="flyer flyer--back" aria-label="Flyer back">
  <div class="quote-band"></div>
  <p class="quote">"She's a beautiful child', isn't she?<br>She's the cause of all the trouble.</p>

  <div class="stain" role="img" aria-label="Soft red watercolour wash"></div>

  <p class="blurb blurb--intro">Hollow Lantern brings back Newcastle's hidden past, the forgotten past, the dark past that may not want to be remembered.</p>

  <div class="tram-photo" role="img" aria-label="Sepia photograph of a tram on a rainy street with a lone figure"></div>

  <p class="blurb blurb--body">Real stories from the streets around you. Discover the histories you won't hear anywhere else. The forgotten stories of yesteryear finally get a chance to be told. Through you they get to live again.</p>

  <div class="brand brand--footer">
    <span class="brand__ring"></span>
    <span class="brand__name">Hollow Lantern</span>
  </div>

  <div class="web-bar">WWW.HOLLOWLANTERN-WALKS.COM.AU</div>
</section>

</body>
</html>
```